Your Joint Helper - Orthopedic needs from one site

We need slides that help to educate users, interest investors and allow the complexity of the entire continuum of care to be explained so anyone can understand. Your Joint Helper is a Varomin Health Company. Yourjointhelperhub.example. We allow people to evaluate, educate and engage with providers from one site. Simplyfying orthopedic care and wellness from one site. Patients, doctors, personal trainers, therapist, nutritionist, yoga, gyms, athletic trainers and more can connect from one site

Target Market(s)

Investors, Patients, Doctors and wellness providers

Industry/Entity Type

Healthcare

Requirements
Must have
• Investor slides, sales slides, education, process....

```html
<!DOCTYPE html>
<html lang="en">
<head>
<meta charset="utf-8">
<title>Your Joint Helper – Slide Deck Overview</title>
<link href="https://fonts.googleapis.com/css2?family=Nunito+Sans:ital,wght@0,400;0,600;0,700;0,800;0,900;1,800;1,900&display=swap" rel="stylesheet">
<style>
:root{
  --navy:#0c2a5b;
  --navy-deep:#081d42;
  --blue:#1f6fc1;
  --sky:#3a8fd8;
  --green:#6cc04a;
  --teal:#3dd0c8;
  --ink:#1a2233;
  --muted:#6b7280;
  --line:#e5e8ee;
  --page:#eef0f3;
}
*{box-sizing:border-box;margin:0;padding:0}
html,body{width:887px;height:1200px;overflow:hidden;background:var(--page)}
body{font-family:"Nunito Sans",Arial,sans-serif;color:var(--ink);position:relative}
.slide{position:absolute;width:290px;height:163px;overflow:hidden;background:#fff;box-shadow:0 1px 3px rgba(0,0,0,.18)}
.abs{position:absolute}
.photo{position:absolute;background:radial-gradient(circle at 60% 40%,#5d8fc9 0%,#1d4a86 40%,#0b2551 100%)}
.photo.light{background:radial-gradient(circle at 55% 45%,#d7e6f6 0%,#8fb3db 45%,#3c6aa5 100%)}
.navy-bg{background:linear-gradient(160deg,#173f7a,#0a2350)}
.h-title{position:absolute;font-weight:800;color:var(--navy);line-height:1.05}
.small{position:absolute;font-size:4.2px;line-height:1.45;color:#555}
.small.white{color:#e6ecf5}
.pill{position:absolute;height:8px;border-radius:4px;font-size:3.6px;color:#fff;display:flex;align-items:center;justify-content:center}
.pill.green{background:var(--green)}
.pill.navy{background:var(--navy)}
.foot-brand{position:absolute;left:7px;bottom:6px;font-size:3.8px;font-weight:800;color:var(--navy);display:flex;align-items:center;gap:2px}
.foot-brand i{width:4px;height:4px;background:var(--green);display:inline-block}
.foot-partner{position:absolute;right:8px;bottom:6px;font-size:4.4px;font-weight:800;color:var(--navy)}
.foot-copy{position:absolute;left:190px;bottom:8px;font-size:2.6px;color:#777}
.foot-rule{position:absolute;left:52px;right:110px;bottom:9px;height:2px;background:#f0f2f5}
.page-no{position:absolute;right:8px;top:6px;font-size:2.6px;color:#999}
.card{position:absolute;background:#fff;box-shadow:0 1px 4px rgba(0,0,0,.15);border-radius:2px}
.svc-title{font-size:4.2px;font-weight:800;color:var(--navy);margin:14px 0 2px 6px}
.svc-text{font-size:3px;color:#666;margin:0 6px;line-height:1.4}
.logo-box{position:absolute;width:62px;height:34px;background:#fff;border-radius:2px;box-shadow:0 1px 3px rgba(0,0,0,.15);font-size:9px;font-weight:800;color:#222;display:flex;align-items:center;justify-content:center}
.team-box{position:absolute;left:22px;width:60px;height:55px;background:var(--navy-deep);color:var(--green);font-size:8px;line-height:1.1;display:flex;align-items:center;justify-content:center;text-align:center}
.member{position:absolute;width:50px;text-align:center}
.member b{display:block;width:20px;height:20px;border-radius:50%;background:#8796ac;margin:0 auto 4px}
.member span{display:block;font-size:4px;color:var(--navy)}
.member em{display:block;font-size:3.4px;color:#999;font-style:normal}
.num-box{position:absolute;width:42px;height:28px;border:1px solid var(--navy);text-align:center;font-size:9px;font-weight:800;color:var(--navy);padding-top:4px;line-height:1}
.num-box small{display:block;font-size:3px;font-weight:400;color:#999;margin-top:3px}
.num-box.green{background:var(--green);border-color:var(--green);color:#fff}
.num-box.green small{color:#eaf6e3}
.month{position:absolute;top:50px;height:7px;width:19.5px;font-size:3.6px;font-weight:800;color:#fff;display:flex;align-items:center;justify-content:center}
.task{position:absolute;height:4.5px;font-size:2.8px;color:#fff;display:flex;align-items:center;justify-content:center}
.task-note{position:absolute;font-size:2.6px;color:#999}
.info-head{position:absolute;font-size:4.4px;font-weight:800;color:var(--navy)}
.info-text{position:absolute;font-size:3px;color:#666;line-height:1.4;width:72px}
</style>
</head>
<body>

<!-- Row 1 -->
<section class="slide" style="left:3px;top:9px">
  <div class="abs" style="left:14px;top:8px;font-size:5px;font-weight:800;color:var(--navy)">Your Joint Helper</div>
  <div class="abs" style="left:66px;top:8px;font-size:5px;font-weight:800;color:var(--navy)">Varomin</div>
  <div class="abs" style="right:6px;top:10px;font-size:4px;font-weight:700;color:var(--green)">Yourjointhelperhub.example</div>
  <div class="photo" role="img" aria-label="Photo of a hand touching a glowing digital skeleton display" style="left:0;top:27px;width:290px;height:136px"></div>
  <div class="abs" style="left:27px;top:61px;font-size:7px;color:var(--green)">Evaluate, educate and engage with providers</div>
  <div class="abs" style="left:27px;top:72px;font-size:15.5px;font-weight:800;color:#fff;line-height:1.13">Simplyfying orthopedic care<br>and wellness from one site</div>
  <div class="pill green" style="left:27px;top:116px;width:40px">October 14 2022</div>
</section>

<section class="slide" style="left:298px;top:9px">
  <div class="photo" role="img" aria-label="Photo of a digital anatomy display" style="left:188px;top:0;width:102px;height:125px"></div>
  <div class="h-title" style="left:10px;top:16px;font-size:12px">Agenda</div>
  <div class="card" style="left:78px;top:25px;width:174px;height:112px;padding:9px 12px">
    <div style="font-size:4.3px;line-height:13.8px;color:#333">
      <div><b style="color:var(--navy);display:inline-block;width:19px">01</b>Lorem ipsum dolor sit amet</div>
      <div><b style="color:var(--navy);display:inline-block;width:19px">02</b>Lorem ipsum dolor sit amet</div>
      <div><b style="color:var(--navy);display:inline-block;width:19px">03</b>Lorem ipsum dolor sit amet</div>
      <div><b style="color:var(--navy);display:inline-block;width:19px">04</b>Lorem ipsum dolor sit amet</div>
      <div><b style="color:var(--navy);display:inline-block;width:19px">05</b>Lorem ipsum dolor sit amet</div>
      <div><b style="color:var(--navy);display:inline-block;width:19px">06</b>Lorem ipsum dolor sit amet</div>
      <div><b style="color:var(--navy);display:inline-block;width:19px">07</b>Lorem ipsum dolor sit amet</div>
    </div>
  </div>
  <div class="foot-brand"><i></i>Your Joint Helper</div><div class="foot-rule"></div>
  <div class="foot-copy">© 2022 Your Joint Helper. All Rights Reserved</div><div class="foot-partner">Varomin</div>
</section>

<section class="slide" style="left:593px;top:9px">
  <div class="page-no">Page 3</div>
  <div class="photo" role="img" aria-label="Photo of an open hand beneath a glowing body scan" style="left:14px;top:17px;width:217px;height:136px"></div>
  <div class="card" style="left:145px;top:36px;width:120px;height:93px"></div>
  <div class="h-title" style="left:161px;top:51px;font-size:12.5px">About<br>Us</div>
  <div class="small" style="left:162px;top:83px;width:88px"><b style="color:#222">Lorem ipsum</b> dolor sit amet, consectetuer adipiscing elit, sed diam nonummy nibh euismod. Ut wisi enim ad minim veniam, quis nostrud exerci tation ullamcorper suscipit lobortis.</div>
  <div class="foot-copy">© 2022 Your Joint Helper. All Rights Reserved</div><div class="foot-partner">Varomin</div>
</section>

<!-- Row 2 -->
<section class="slide" style="left:3px;top:178px">
  <div class="h-title" style="left:10px;top:36px;font-size:12.5px">Our<br>Project</div>
  <div class="small" style="left:12px;top:70px;width:70px">A wonderful serenity has taken possession of my entire soul, like these sweet mornings of spring which I enjoy with my whole heart. I am alone, and feel the charm</div>
  <div class="pill navy" style="left:16px;top:110px;width:41px">Read more text</div>
  <div class="abs navy-bg" style="left:90px;top:0;width:200px;height:163px"></div>
  <div class="photo light" role="img" aria-label="Photo of a doctor in a hospital corridor" style="left:103px;top:17px;width:76px;height:39px"></div>
  <div class="photo" role="img" aria-label="Photo of two hands with glowing light" style="left:103px;top:62px;width:76px;height:39px"></div>
  <div class="photo" role="img" aria-label="Photo of a finger touching a digital skeleton screen" style="left:103px;top:106px;width:76px;height:39px"></div>
  <div class="abs" style="left:189px;top:22px;color:#fff;font-size:8px">Mar <b>'2022</b></div>
  <div class="small white" style="left:189px;top:35px;width:85px">Startups<br>A wonderful serenity has taken possession of my entire soul, like these sweet mornings.</div>
  <div class="abs" style="left:189px;top:66px;color:#fff;font-size:8px">Apr <b>'2022</b></div>
  <div class="small white" style="left:189px;top:79px;width:85px">Teamwork<br>A wonderful serenity has taken possession of my entire soul, like these sweet mornings.</div>
  <div class="abs" style="left:189px;top:110px;color:#fff;font-size:8px">May <b>'2022</b></div>
  <div class="small white" style="left:189px;top:123px;width:85px">Business Agenda<br>A wonderful serenity has taken possession of my entire soul, like these sweet mornings.</div>
</section>

<section class="slide" style="left:298px;top:178px">
  <div class="photo" role="img" aria-label="Photo of a hand over a blue medical background" style="left:0;top:0;width:290px;height:82px"></div>
  <div class="abs" style="left:0;width:290px;top:14px;text-align:center;font-size:12.5px;font-weight:800;color:#fff">Our Services</div>
  <div class="card" style="left:25px;top:37px;width:77px;height:48px"><div class="svc-title">Service title #1</div><div class="svc-text">A wonderful serenity has taken possession of my entire soul, like these sweet mornings of spring.</div></div>
  <div class="card" style="left:107px;top:37px;width:77px;height:48px"><div class="svc-title">Service title #2</div><div class="svc-text">A wonderful serenity has taken possession of my entire soul, like these sweet mornings of spring.</div></div>
  <div class="card" style="left:189px;top:37px;width:77px;height:48px"><div class="svc-title">Service title #3</div><div class="svc-text">A wonderful serenity has taken possession of my entire soul, like these sweet mornings of spring.</div></div>
  <div class="card" style="left:25px;top:90px;width:77px;height:48px"><div class="svc-title">Service title #4</div><div class="svc-text">A wonderful serenity has taken possession of my entire soul, like these sweet mornings of spring.</div></div>
  <div class="card" style="left:107px;top:90px;width:77px;height:48px"><div class="svc-title">Service title #5</div><div class="svc-text">A wonderful serenity has taken possession of my entire soul, like these sweet mornings of spring.</div></div>
  <div class="card" style="left:189px;top:90px;width:77px;height:48px"><div class="svc-title">Service title #6</div><div class="svc-text">A wonderful serenity has taken possession of my entire soul, like these sweet mornings of spring.</div></div>
  <div class="foot-brand"><i></i>Your Joint Helper</div>
  <div class="foot-copy">© 2022 Your Joint Helper. All Rights Reserved</div><div class="foot-partner">Varomin</div>
</section>

<section class="slide" style="left:593px;top:178px">
  <div class="photo" role="img" aria-label="Dark blue photo of a doctor's hand" style="left:0;top:0;width:290px;height:163px;background:radial-gradient(circle at 50% 50%,#2a5592,#0b2551 75%)"></div>
  <div class="abs" style="left:79px;top:40px;font-size:27px;font-weight:900;font-style:italic;color:#fff;line-height:1">BREAK</div>
  <div class="abs" style="left:123px;top:68px;font-size:27px;font-weight:900;font-style:italic;color:#fff;line-height:1">SLIDE</div>
  <div class="abs" style="left:57px;top:118px;width:12px;height:1px;background:var(--green)"></div>
  <div class="abs" style="left:57px;top:120px;font-size:3.8px;font-style:italic;color:var(--green)">Presentation will continue at</div>
  <div class="abs" style="left:59px;top:126px;font-size:6px;font-style:italic;color:var(--green)">14 : 00</div>
</section>

<!-- Row 3 -->
<section class="slide" style="left:3px;top:347px">
  <div class="h-title" style="left:10px;top:16px;font-size:12.5px">Our Mockup Slide</div>
  <svg class="abs" style="left:0;top:0" width="290" height="163"><polygon points="185,0 290,0 290,163 140,163" fill="var(--navy)"/></svg>
  <div class="photo" role="img" aria-label="Illustration of a desktop monitor showing medical imagery" style="left:140px;top:15px;width:140px;height:128px;border-radius:4px"></div>
  <div class="small" style="left:28px;top:59px;width:80px;font-size:3.4px">A wonderful serenity has taken possession of my entire soul, like these sweet mornings of spring which I enjoy with my whole heart.</div>
  <svg class="abs" style="left:26px;top:82px" width="34" height="34"><circle cx="17" cy="17" r="14" fill="none" stroke="#e8ecf1" stroke-width="1.5"/><circle cx="17" cy="17" r="14" fill="none" stroke="var(--blue)" stroke-width="1.5" stroke-dasharray="66 88" transform="rotate(-90 17 17)"/><text x="17" y="19.5" text-anchor="middle" font-size="7" font-weight="700" fill="var(--green)">75%</text></svg>
  <svg class="abs" style="left:72px;top:82px" width="34" height="34"><circle cx="17" cy="17" r="14" fill="none" stroke="#e8ecf1" stroke-width="1.5"/><circle cx="17" cy="17" r="14" fill="none" stroke="var(--green)" stroke-width="1.5" stroke-dasharray="35 88" transform="rotate(-90 17 17)"/><text x="17" y="19.5" text-anchor="middle" font-size="7" font-weight="700" fill="var(--green)">40%</text></svg>
  <div class="abs" style="left:33px;top:118px;font-size:3px;color:#666">Data title 01</div>
  <div class="abs" style="left:79px;top:118px;font-size:3px;color:#666">Data title 02</div>
  <div class="foot-brand"><i></i>Your Joint Helper</div>
</section>

<section class="slide" style="left:298px;top:347px">
  <div class="page-no">Page 8</div>
  <div class="photo" role="img" aria-label="Illustration of two smartphones showing medical imagery" style="left:38px;top:22px;width:95px;height:118px;border-radius:10px"></div>
  <div class="h-title" style="left:154px;top:50px;font-size:13px">Our App</div>
  <div class="small" style="left:154px;top:73px;width:95px">A wonderful serenity has taken possession of my entire soul, like these sweet mornings of spring which I enjoy with my whole heart. I am alone, and feel the charm</div>
  <div class="pill green" style="left:154px;top:103px;width:40px">Read more text</div>
  <div class="foot-brand"><i></i>Your Joint Helper</div><div class="foot-rule"></div>
  <div class="foot-copy">© 2022 Your Joint Helper. All Rights Reserved</div><div class="foot-partner">Varomin</div>
</section>

<section class="slide" style="left:593px;top:347px">
  <div class="page-no">Page 9</div>
  <div class="h-title" style="left:10px;top:14px;font-size:12.5px">Your Title Here</div>
  <div class="small" style="left:12px;top:31px;width:200px;color:#333">A wonderful serenity has taken possession of my entire soul, like these sweet mornings of spring which I enjoy with my whole heart. I am alone, and feel the charm of existence in this spot.</div>
  <div class="photo" role="img" aria-label="Photo of a finger touching a digital skeleton screen" style="left:90px;top:54px;width:200px;height:77px"></div>
  <div class="abs" style="left:38px;top:75px;width:75px;height:61px;background:var(--navy-deep);padding:10px 8px">
    <div style="font-size:7px;font-weight:800;color:#fff">2022</div>
    <div style="font-size:3px;color:#dde4ef;line-height:1.4">A wonderful serenity has taken possession of my entire soul, like these sweet mornings of spring which I enjoy with my whole heart. I am alone.</div>
  </div>
  <div class="foot-brand"><i></i>Your Joint Helper</div>
  <div class="foot-copy">© 2022 Your Joint Helper. All Rights Reserved</div><div class="foot-partner">Varomin</div>
</section>

<!-- Row 4 -->
<section class="slide" style="left:3px;top:516px">
  <div class="page-no">Page 10</div>
  <div class="team-box" style="top:19px">Surgeon<br>Team</div>
  <div class="team-box" style="top:80px">Neurologist<br>Team</div>
  <div class="member" style="left:98px;top:26px"><b></b><span>Dr. Lena Hart</span><em>Surgeon Doctor</em></div>
  <div class="member" style="left:155px;top:26px"><b></b><span>Dr. Omar Velt</span><em>Surgeon Doctor</em></div>
  <div class="member" style="left:211px;top:26px"><b></b><span>Dr. Ivo Brandt</span><em>Surgeon Doctor</em></div>
  <div class="member" style="left:98px;top:87px"><b></b><span>Dr. Sira Noll</span><em>Neurologist Doctor</em></div>
  <div class="member" style="left:155px;top:87px"><b></b><span>Dr. Teo Marlin</span><em>Neurologist Doctor</em></div>
  <div class="member" style="left:211px;top:87px"><b></b><span>Dr. Ada Quist</span><em>Neurologist Doctor</em></div>
  <div class="foot-brand"><i></i>Your Joint Helper</div>
  <div class="foot-copy">© 2022 Your Joint Helper. All Rights Reserved</div><div class="foot-partner">Varomin</div>
</section>

<section class="slide" style="left:298px;top:516px">
  <div class="photo" role="img" aria-label="Photo of a hand reaching toward a glowing body scan" style="left:0;top:0;width:290px;height:49px"></div>
  <div class="h-title" style="left:22px;top:61px;font-size:12.5px">Your Title<br>Here</div>
  <div class="small" style="left:23px;top:91px;width:96px;color:#333">A wonderful serenity has taken possession of my entire soul, like these sweet mornings of spring which I enjoy with my whole heart. I am alone, and feel the charm</div>
  <div class="pill green" style="left:23px;top:124px;width:40px">Read more text</div>
  <div class="card" style="left:122px;top:27px;width:74px;height:97px;text-align:center">
    <svg style="margin-top:16px" width="34" height="34"><circle cx="17" cy="17" r="15" fill="#f1f3f6"/><circle cx="17" cy="17" r="15" fill="none" stroke="var(--navy)" stroke-width="1" stroke-dasharray="45 94" transform="rotate(-90 17 17)"/><text x="17" y="19.5" text-anchor="middle" font-size="7" font-weight="800" fill="var(--navy)">48%</text></svg>
    <div style="font-size:5px;color:#222;margin-top:8px">First value</div>
    <div style="font-size:3px;color:#666;padding:0 5px;line-height:1.4">A wonderful serenity has taken possession of my entire soul, like these sweet mornings of spring.</div>
  </div>
  <div class="abs" style="left:200px;top:27px;width:75px;height:97px;background:var(--navy);text-align:center">
    <svg style="margin-top:16px" width="34" height="34"><circle cx="17" cy="17" r="15" fill="#163a72"/><circle cx="17" cy="17" r="15" fill="none" stroke="#fff" stroke-width="1" stroke-dasharray="66 94" transform="rotate(-90 17 17)"/><text x="17" y="19.5" text-anchor="middle" font-size="7" font-weight="800" fill="#fff">70%</text></svg>
    <div style="font-size:5px;color:#fff;margin-top:8px">Second value</div>
    <div style="font-size:3px;color:#d7e0ee;padding:0 5px;line-height:1.4">A wonderful serenity has taken possession of my entire soul, like these sweet mornings of spring.</div>
  </div>
  <div class="foot-brand"><i></i>Your Joint Helper</div>
  <div class="foot-copy">© 2022 Your Joint Helper. All Rights Reserved</div><div class="foot-partner">Varomin</div>
</section>

<section class="slide" style="left:593px;top:516px">
  <div class="page-no">Page 12</div>
  <div class="h-title" style="left:0;width:290px;text-align:center;top:18px;font-size:12.5px">Project Data Report</div>
  <div class="small" style="left:70px;top:43px;width:150px;text-align:center;color:#333;font-size:3.6px">Bring to the table win-win survival strategies to ensure proactive domination. At the end of the day, going forward, a new normal that has evolved from generation.</div>
  <div class="abs" style="left:30px;top:80px;font-size:3.2px;color:#333">March Data report</div>
  <div class="abs" style="left:90px;top:80px;font-size:3.2px;color:#333">March Data report</div>
  <div class="abs" style="left:149px;top:80px;font-size:3.2px;color:#333">2019 Data report</div>
  <svg class="abs" style="left:38px;top:89px" width="32" height="32"><circle cx="16" cy="16" r="12" fill="none" stroke="var(--blue)" stroke-width="5"/><circle cx="16" cy="16" r="12" fill="none" stroke="var(--green)" stroke-width="5" stroke-dasharray="50 76" transform="rotate(-90 16 16)"/><text x="16" y="18" text-anchor="middle" font-size="4.5" fill="#333">66%</text></svg>
  <svg class="abs" style="left:96px;top:89px" width="32" height="32"><circle cx="16" cy="16" r="12" fill="none" stroke="var(--blue)" stroke-width="5"/><circle cx="16" cy="16" r="12" fill="none" stroke="var(--green)" stroke-width="5" stroke-dasharray="62 76" transform="rotate(-90 16 16)"/><text x="16" y="18" text-anchor="middle" font-size="4.5" fill="#333">82%</text></svg>
  <div class="abs" style="left:36px;top:125px;font-size:2.8px;color:#999;line-height:1.4">■ Data 1 &nbsp; ■ Data 2<br>■ Data 3 &nbsp; ■ Data 4</div>
  <div class="abs" style="left:94px;top:125px;font-size:2.8px;color:#999;line-height:1.4">■ Data 1 &nbsp; ■ Data 2<br>■ Data 3 &nbsp; ■ Data 4</div>
  <svg class="abs" style="left:155px;top:90px" width="112" height="34">
    <defs><linearGradient id="areaFill" x1="0" x2="1"><stop offset="0" stop-color="var(--green)"/><stop offset="1" stop-color="var(--blue)"/></linearGradient></defs>
    <polygon points="0,34 0,14 20,20 42,4 62,22 84,10 100,18 112,2 112,34" fill="url(#areaFill)"/>
    <polygon points="0,14 20,20 42,4 62,14 84,12 100,18 112,2 100,14 84,10 62,22 42,4" fill="var(--navy)" opacity=".9"/>
  </svg>
  <div class="abs" style="left:150px;top:129px;width:124px;display:flex;justify-content:space-between;font-size:2.8px;color:#999"><span>Data 1</span><span>Data 2</span><span>Data 3</span><span>Data 4</span><span>Data 5</span><span>Data 6</span></div>
  <div class="foot-brand"><i></i>Your Joint Helper</div>
  <div class="foot-copy">© 2022 Your Joint Helper. All Rights Reserved</div><div class="foot-partner">Varomin</div>
</section>

<!-- Row 5 -->
<section class="slide" style="left:3px;top:685px">
  <div class="page-no">Page 13</div>
  <div class="h-title" style="left:0;width:290px;text-align:center;top:18px;font-size:12.5px">The Business Data Report</div>
  <div class="abs navy-bg" style="left:0;top:40px;width:290px;height:74px"></div>
  <div class="abs" style="left:16px;top:55px;font-size:11px;color:#fff">2023</div>
  <div class="small white" style="left:48px;top:55px;width:90px;font-size:3.6px">Bring to the table win-win survival strategies to ensure proactive domination.</div>
  <div class="small white" style="left:16px;top:75px;width:70px;font-size:3px">Bring to the table win-win survival strategies to ensure proactive domination. At the end of the day, going forward, a new normal that has evolved from generation.</div>
  <div class="card" style="left:160px;top:43px;width:127px;height:74px">
    <svg width="127" height="74" font-size="3" fill="#999">
      <text x="10" y="13">Furniture</text><text x="10" y="25">Renovation</text><text x="10" y="37">Decoration</text><text x="10" y="49">Interior</text>
      <rect x="34" y="10" width="40" height="3" fill="var(--navy)"/><rect x="74" y="10" width="22" height="3" fill="var(--blue)"/><rect x="96" y="10" width="6" height="3" fill="var(--green)"/>
      <rect x="34" y="22" width="34" height="3" fill="var(--navy)"/><rect x="68" y="22" width="18" height="3" fill="var(--blue)"/><rect x="86" y="22" width="22" height="3" fill="var(--green)"/>
      <rect x="34" y="34" width="22" height="3" fill="var(--navy)"/><rect x="56" y="34" width="34" height="3" fill="var(--blue)"/><rect x="90" y="34" width="10" height="3" fill="var(--green)"/>
      <rect x="34" y="46" width="56" height="3" fill="var(--navy)"/><rect x="90" y="46" width="10" height="3" fill="var(--blue)"/><rect x="100" y="46" width="12" height="3" fill="var(--green)"/>
      <text x="34" y="62">0</text><text x="61" y="62">5</text><text x="88" y="62">10</text><text x="115" y="62">15</text>
    </svg>
  </div>
  <div class="card" style="left:98px;top:63px;width:122px;height:77px">
    <svg width="122" height="77" font-size="3" fill="#999">
      <text x="10" y="14">Furniture</text><text x="8" y="25">Renovation</text><text x="8" y="36">Decoration</text><text x="14" y="47">Interior</text>
      <rect x="28" y="8" width="22" height="2.5" fill="var(--green)"/><rect x="28" y="11" width="36" height="2.5" fill="var(--navy)"/><rect x="28" y="14" width="12" height="2.5" fill="var(--blue)"/>
      <rect x="28" y="20" width="18" height="2.5" fill="var(--green)"/><rect x="28" y="23" width="24" height="2.5" fill="var(--navy)"/><rect x="28" y="26" width="8" height="2.5" fill="var(--blue)"/>
      <rect x="28" y="31" width="10" height="2.5" fill="var(--green)"/><rect x="28" y="34" width="28" height="2.5" fill="var(--blue)"/><rect x="28" y="37" width="14" height="2.5" fill="var(--navy)"/>
      <rect x="28" y="42" width="10" height="2.5" fill="var(--green)"/><rect x="28" y="45" width="56" height="2.5" fill="var(--navy)"/>
      <text x="28" y="64">0</text><text x="55" y="64">5</text><text x="82" y="64">10</text><text x="109" y="64">15</text>
    </svg>
  </div>
  <div class="foot-brand"><i></i>Your Joint Helper</div>
  <div class="foot-copy">© 2022 Your Joint Helper. All Rights Reserved</div><div class="foot-partner">Varomin</div>
</section>

<section class="slide" style="left:298px;top:685px">
  <div class="photo" role="img" aria-label="Blue medical photo background" style="left:0;top:0;width:290px;height:85px"></div>
  <div class="abs" style="left:0;width:290px;top:19px;text-align:center;font-size:12px;font-weight:800;color:#fff">Our Partner</div>
  <div class="logo-box" style="left:10px;top:53px">LOGO</div>
  <div class="logo-box" style="left:79px;top:53px">LOGO</div>
  <div class="logo-box" style="left:148px;top:53px">LOGO</div>
  <div class="logo-box" style="left:217px;top:53px">LOGO</div>
  <div class="logo-box" style="left:10px;top:96px">LOGO</div>
  <div class="logo-box" style="left:79px;top:96px">LOGO</div>
  <div class="logo-box" style="left:148px;top:96px">LOGO</div>
  <div class="logo-box" style="left:217px;top:96px">LOGO</div>
  <div class="foot-brand"><i></i>Your Joint Helper</div>
  <div class="foot-copy">© 2022 Your Joint Helper. All Rights Reserved</div><div class="foot-partner">Varomin</div>
</section>

<section class="slide" style="left:593px;top:685px">
  <div class="photo" role="img" aria-label="Blue photo of a doctor" style="left:0;top:0;width:290px;height:163px"></div>
  <div class="abs" style="left:0;width:290px;top:13px;text-align:center;font-size:11.5px;font-weight:800;color:#fff">Client Testimonial</div>
  <div class="abs" style="left:38px;top:52px;width:214px;height:82px;background:rgba(255,255,255,.35)"></div>
  <div class="abs" style="left:50px;top:44px;width:190px;height:99px;background:#fff"></div>
  <div class="abs" style="left:134px;top:51px;width:22px;height:22px;border-radius:50%;background:linear-gradient(#c9d4e2,#7d8fa8)" role="img" aria-label="Client portrait"></div>
  <div class="abs" style="left:0;width:290px;top:77px;text-align:center;font-size:6.5px;font-weight:800">Name Surname</div>
  <div class="abs" style="left:0;width:290px;top:86px;text-align:center;font-size:2.8px;color:var(--blue)">Title</div>
  <div class="small" style="left:85px;top:93px;width:120px;text-align:center;font-size:3.2px">Ut wisi enim ad minim veniam, quis nostrud exerci tation ullamcorper suscipit lobortis nisl ut aliquip ex ea commodo consequat. Lorem ipsum dolor sit amet.</div>
  <div class="abs" style="left:0;width:290px;top:119px;text-align:center;font-size:5px;color:#f5b301">★★★★★</div>
  <svg class="abs" style="left:14px;top:86px" width="11" height="11"><circle cx="5.5" cy="5.5" r="5" fill="none" stroke="#fff" stroke-width=".7"/><path d="M6.5 3.5 4.5 5.5 6.5 7.5" fill="none" stroke="#fff" stroke-width=".8"/></svg>
  <svg class="abs" style="left:265px;top:86px" width="11" height="11"><circle cx="5.5" cy="5.5" r="5" fill="none" stroke="#fff" stroke-width=".7"/><path d="M4.5 3.5 6.5 5.5 4.5 7.5" fill="none" stroke="#fff" stroke-width=".8"/></svg>
</section>

<!-- Row 6 -->
<section class="slide" style="left:3px;top:854px">
  <div class="page-no">Page 16</div>
  <div class="h-title" style="left:0;width:290px;text-align:center;top:15px;font-size:12.5px">Our statistic</div>
  <svg class="abs" style="left:20px;top:43px" width="130" height="100" font-size="3.6" fill="#333">
    <ellipse cx="62" cy="62" rx="42" ry="21" fill="#2e7d34"/>
    <path d="M62 52 L62 31 A42 21 0 1 1 34 67 Z" fill="var(--green)"/>
    <path d="M58 50 L16 48 A42 21 0 0 1 30 36 Z" fill="#8fc63e"/>
    <path d="M58 49 L30 35 A42 21 0 0 1 45 28 Z" fill="var(--blue)"/>
    <path d="M58 48 L45 27 A42 21 0 0 1 60 26 Z" fill="var(--teal)"/>
    <text x="30" y="11">Data 3</text><text x="33" y="16">9%</text>
    <text x="14" y="22">Data 3</text><text x="17" y="27">10%</text>
    <text x="0" y="57">Data 2</text><text x="3" y="62">23%</text>
    <text x="109" y="57">Data 1</text><text x="112" y="62">58%</text>
    <text x="50" y="98" fill="#666">■ Data 1 &#160; ■ Data 2</text>
  </svg>
  <div class="abs" style="left:173px;top:55px;font-size:5px;font-weight:800;color:var(--navy)">Our Growth</div>
  <div class="small" style="left:173px;top:69px;width:98px;color:#333">Ut wisi enim ad minim veniam, quis nostrud exerci tation ullamcorper suscipit lobortis nisl ut aliquip ex ea commodo consequat. Lorem ipsum dolor sit amet, consectetuer adipiscing elit.</div>
  <div class="abs" style="left:177px;top:102px;width:18px;height:18px;border-radius:50%;background:var(--navy-deep)"></div>
  <div class="abs" style="left:211px;top:102px;width:18px;height:18px;border-radius:50%;background:var(--navy-deep)"></div>
  <div class="abs" style="left:245px;top:102px;width:18px;height:18px;border-radius:50%;background:var(--navy-deep)"></div>
  <div class="abs" style="left:172px;top:124px;width:100px;display:flex;justify-content:space-between;font-size:3.4px;text-align:center;color:#333"><span>Ut wisi enim<br>ad minim</span><span>Ut wisi enim<br>ad minim</span><span>Ut wisi enim<br>ad minim</span></div>
  <div class="foot-brand"><i></i>Your Joint Helper</div>
  <div class="foot-copy">© 2022 Your Joint Helper. All Rights Reserved</div><div class="foot-partner">Varomin</div>
</section>

<section class="slide" style="left:298px;top:854px">
  <div class="page-no">Page 17</div>
  <div class="abs" role="img" aria-label="Isometric illustration of a tablet with a doctor profile, medical kit and charts" style="left:18px;top:30px;width:130px;height:95px;background:linear-gradient(135deg,#d8eef0,#7cc6c2 55%,#2f6fb3);border-radius:6px"></div>
  <div class="h-title" style="left:154px;top:36px;font-size:13px">Our Infographic</div>
  <div class="num-box" style="left:153px;top:61px">1287<small>Your Title Here</small></div>
  <div class="num-box green" style="left:203px;top:61px">500<small>Your Title Here</small></div>
  <div class="num-box" style="left:153px;top:96px">1348+<small>Your Title Here</small></div>
  <div class="num-box" style="left:203px;top:96px">2870+<small>Your Title Here</small></div>
  <div class="foot-brand"><i></i>Your Joint Helper</div>
  <div class="foot-copy">© 2022 Your Joint Helper. All Rights Reserved</div><div class="foot-partner">Varomin</div>
</section>

<section class="slide" style="left:593px;top:854px">
  <div class="page-no">Page 18</div>
  <div class="h-title" style="left:0;width:290px;text-align:center;top:17px;font-size:12.5px">Infographic</div>
  <svg class="abs" style="left:100px;top:43px" width="90" height="90" font-size="4.5" fill="#555" text-anchor="middle">
    <g fill="none" stroke-width="7">
      <circle cx="45" cy="45" r="38" stroke="var(--navy)" stroke-dasharray="47 239" transform="rotate(-162 45 45)"/>
      <circle cx="45" cy="45" r="38" stroke="var(--teal)" stroke-dasharray="47 239" transform="rotate(-90 45 45)"/>
      <circle cx="45" cy="45" r="38" stroke="var(--green)" stroke-dasharray="47 239" transform="rotate(-18 45 45)"/>
      <circle cx="45" cy="45" r="38" stroke="#8fc63e" stroke-dasharray="47 239" transform="rotate(54 45 45)"/>
      <circle cx="45" cy="45" r="38" stroke="var(--blue)" stroke-dasharray="47 239" transform="rotate(126 45 45)"/>
    </g>
    <circle cx="45" cy="45" r="28" fill="#f4f5f7"/>
    <circle cx="45" cy="45" r="12" fill="#fff" stroke="#ddd" stroke-width=".5"/>
    <path d="M40 43 h3 l6 -4 v12 l-6 -4 h-3 z" fill="#555"/>
    <text x="30" y="28">01</text><text x="60" y="28">05</text><text x="25" y="54">02</text><text x="65" y="54">04</text><text x="45" y="69">03</text>
  </svg>
  <div class="info-head" style="left:62px;top:52px">Heading Here</div>
  <div class="info-text" style="left:17px;top:58px;text-align:right">Sed ut perspiciatis unde omnis iste natus error sit voluptatem accusantium doloremque laudantium.</div>
  <div class="info-head" style="left:197px;top:52px">Heading Here</div>
  <div class="info-text" style="left:197px;top:58px">Sed ut perspiciatis unde omnis iste natus error sit voluptatem accusantium doloremque laudantium.</div>
  <div class="info-head" style="left:62px;top:96px">Heading Here</div>
  <div class="info-text" style="left:17px;top:102px;text-align:right">Sed ut perspiciatis unde omnis iste natus error sit voluptatem accusantium doloremque laudantium.</div>
  <div class="info-head" style="left:196px;top:96px">Heading Here</div>
  <div class="info-text" style="left:196px;top:102px">Sed ut perspiciatis unde omnis iste natus error sit voluptatem accusantium doloremque laudantium.</div>
  <div class="info-head" style="left:163px;top:133px;color:var(--green)">Heading Here</div>
  <div class="info-text" style="left:163px;top:139px">Sed ut perspiciatis unde omnis iste natus error sit voluptatem.</div>
  <div class="foot-brand"><i></i>Your Joint Helper</div><div class="foot-partner">Varomin</div>
</section>

<!-- Row 7 -->
<section class="slide" style="left:3px;top:1023px">
  <div class="page-no">Page 19</div>
  <div class="h-title" style="left:0;width:290px;text-align:center;top:17px;font-size:12.5px">Available On App</div>
  <div class="abs" style="left:192px;top:41px;font-size:5.5px;font-weight:800;font-style:italic;line-height:1.2">“Created For The Bliss<br>Of Souls Like Mine.</div>
  <div class="abs" style="left:187px;top:62px;width:103px;height:72px;background:var(--navy-deep);padding:12px 0 0 19px;color:#fff">
    <div style="font-size:11px;font-weight:800">80% ↑</div>
    <div style="font-size:5px;margin:2px 0 3px">Maximum Speed</div>
    <div style="font-size:4.2px;line-height:1.35;width:70px">A wonderful serenity has taken possession of my entire soul, like these sweet</div>
  </div>
  <div class="abs" role="img" aria-label="Illustration of a hand holding a smartphone with an app screen" style="left:115px;top:55px;width:60px;height:108px;background:linear-gradient(180deg,#5c6470 0%,#7d8794 45%,#f4cf9a 70%,#f1c68e 100%);border-radius:6px 6px 0 0"></div>
  <div class="abs" style="left:38px;top:62px;width:49px;text-align:right;font-size:4px;font-weight:800;line-height:1.1">Insert Your Amazing Statement Here</div>
  <div class="small" style="left:20px;top:72px;width:67px;text-align:right">A wonderful serenity has taken possession of my entire soul, like these sweet</div>
  <div class="abs" style="left:38px;top:106px;width:49px;text-align:right;font-size:4px;font-weight:800;line-height:1.1">Insert Your Amazing Statement Here</div>
  <div class="small" style="left:20px;top:116px;width:67px;text-align:right">A wonderful serenity has taken possession of my entire soul, like these sweet</div>
  <svg class="abs" style="left:95px;top:68px" width="30" height="50"><circle cx="4" cy="2" r="2" fill="#ddd"/><line x1="6" y1="2" x2="30" y2="2" stroke="#ddd" stroke-width=".5"/><circle cx="4" cy="46" r="2" fill="#ddd"/><line x1="6" y1="46" x2="30" y2="46" stroke="#ddd" stroke-width=".5"/></svg>
  <div class="foot-brand"><i></i>Your Joint Helper</div>
  <div class="foot-copy">© 2022 Your Joint Helper. All Rights Reserved</div><div class="foot-partner">Varomin</div>
</section>

<section class="slide" style="left:298px;top:1023px">
  <div class="page-no">Page 20</div>
  <div class="h-title" style="left:0;width:290px;text-align:center;top:17px;font-size:12.5px">Process Infographic</div>
  <div class="month" style="left:28px;background:var(--navy)">JAN</div>
  <div class="month" style="left:47.5px;background:var(--navy)">FEB</div>
  <div class="month" style="left:67px;background:var(--navy)">MAR</div>
  <div class="month" style="left:86.5px;background:var(--navy)">APR</div>
  <div class="month" style="left:106px;background:var(--navy)">MAY</div>
  <div class="month" style="left:125.5px;background:var(--navy)">JUN</div>
  <div class="month" style="left:145px;background:var(--blue)">JUL</div>
  <div class="month" style="left:164.5px;background:var(--blue)">AUG</div>
  <div class="month" style="left:184px;background:var(--blue)">SEP</div>
  <div class="month" style="left:203.5px;background:var(--blue)">OCT</div>
  <div class="month" style="left:223px;background:var(--blue)">NOV</div>
  <div class="month" style="left:242.5px;background:var(--blue)">DEC</div>
  <svg class="abs" style="left:0;top:57px" width="290" height="90">
    <polygon points="95,36 248,36 248,28 262,44 248,60 248,52 95,52" fill="#eceef1"/>
    <g stroke-width=".5">
      <line x1="98" y1="0" x2="98" y2="30" stroke="var(--navy)"/>
      <line x1="132" y1="0" x2="132" y2="40" stroke="var(--navy)"/>
      <line x1="157" y1="0" x2="157" y2="50" stroke="var(--green)"/>
      <line x1="203" y1="0" x2="203" y2="62" stroke="var(--green)"/>
      <line x1="236" y1="0" x2="236" y2="78" stroke="var(--teal)"/>
    </g>
  </svg>
  <div class="task" style="left:62px;top:82px;width:36px;background:var(--navy)">Task</div><div class="task-note" style="left:99px;top:83px">Date start-end</div>
  <div class="task" style="left:110px;top:92px;width:22px;background:var(--navy)">Task</div><div class="task-note" style="left:133px;top:93px">Date start-end</div>
  <div class="task" style="left:123px;top:103px;width:34px;background:var(--green)">Task</div><div class="task-note" style="left:158px;top:104px">Date start-end</div>
  <div class="task" style="left:157px;top:114px;width:46px;background:var(--green)">Task</div><div class="task-note" style="left:204px;top:115px">Date start-end</div>
  <div class="task" style="left:210px;top:130px;width:26px;background:var(--teal)">Task</div><div class="task-note" style="left:237px;top:131px">Date start-end</div>
  <div class="abs" style="left:28px;top:105px;font-size:4px;font-weight:800;line-height:1.1">Insert Your Amazing<br>Statement Here</div>
  <div class="small" style="left:28px;top:116px;width:65px;color:var(--blue)">A wonderful serenity has taken possession of my entire soul, like these sweet</div>
  <div class="foot-brand"><i></i>Your Joint Helper</div>
  <div class="foot-copy">© 2022 Your Joint Helper. All Rights Reserved</div><div class="foot-partner">Varomin</div>
</section>

<section class="slide" style="left:593px;top:1023px">
  <div class="abs" style="left:57px;top:15px;width:5px;height:5px;background:var(--green)"></div>
  <div class="abs" style="left:65px;top:10px;font-size:9px;font-weight:800;color:var(--navy);line-height:1.05">Your Joint<br>Helper</div>
  <div class="abs" style="left:180px;top:15px;font-size:11px;font-weight:800;color:var(--navy)">Varomin</div>
  <div class="photo" role="img" aria-label="Photo of a hand touching a glowing digital anatomy display" style="left:0;top:53px;width:290px;height:110px"></div>
  <div class="abs" style="left:0;width:290px;top:78px;text-align:center;font-size:24px;font-weight:800;color:#fff">Thank you</div>
  <div class="pill green" style="left:118px;top:116px;width:54px">Yourjointhelperhub.example</div>
</section>

</body>
</html>
```